Prestige Car Bodyshop Business Card

We are a car bodyshop based in the UK. Our customer base is mainly prestige high-value vehicles. I am looking for a classy and stylish business card design for my staff to give out to customers, with their direct email and phone number, as well as our main email and phone number with address details

I am also looking to have a general business card design with just our main company address and contact details, but also have a space to add a manufacturer approval logo (i.e Velmora, Orek, Tovalo etc... logo) in the corner somewhere.

I do not particularly want any outlines or pictures of cars on the card, I would just like a quality high-end look.

Please feel free to get in touch if you have any questions or queries?

Many Thanks

Malcolm

Target Market(s)

Prestige vehicle owners

Industry/Entity Type

Automotive

Contact Information for Business Card

I am looking for a classy and stylish business card design for my staff to give out to customers, with their direct email and phone number, as well as our main email and phone number with address details

Font styles to use
Sans Serif

Colors

Designer to choose colors to be used in the design.

Requirements
Nice to have
• I do not particularly want any outlines or pictures of cars on the card, I would just like a quality high-end look.

```html
<!DOCTYPE html>
<html lang="en">
<head>
<meta charset="utf-8">
<title>Halden Rowe Business Card</title>
<link rel="stylesheet" href="https://fonts.googleapis.com/css2?family=Oswald:wght@500&family=Roboto:wght@400;700&display=swap">
<style>
  :root {
    --page-bg: #ececee;
    --card-white: #ffffff;
    --brand-blue: #1a6fc4;
    --brand-deep: #0d4f9a;
    --brand-mid: #2a86d6;
    --text-dark: #3a3d42;
    --rule-grey: #c9ccd1;
    --badge-grey: #9aa0a8;
  }
  * { margin: 0; padding: 0; box-sizing: border-box; }
  html, body {
    width: 1200px; height: 2441px; overflow: hidden;
    background: var(--page-bg);
  }
  .card {
    position: absolute; left: 60px; top: 917px;
    width: 1080px; height: 606px;
    background: var(--card-white);
    box-shadow: 0 6px 18px rgba(0,0,0,0.18);
    overflow: hidden;
  }
  .card-shapes { position: absolute; inset: 0; }
  .staff-name {
    position: absolute; left: 0; width: 540px; top: 138px;
    text-align: center; color: #fff;
    font-family: "Oswald", sans-serif; font-weight: 500;
    font-size: 34px; letter-spacing: 5px; line-height: 1;
  }
  .staff-role {
    position: absolute; left: 0; width: 540px; top: 184px;
    text-align: center; color: #fff;
    font-family: "Roboto", sans-serif; font-size: 13px; letter-spacing: 8px;
  }
  .contact {
    position: absolute; left: 82px; top: 294px;
    font-family: "Roboto", sans-serif; font-size: 17px; line-height: 21px;
    color: var(--text-dark);
  }
  .contact .company { font-weight: 700; }
  .contact .label { display: inline-block; width: 58px; }
  .brand {
    position: absolute; left: 768px; top: 104px;
    display: flex; align-items: center; gap: 14px;
  }
  .brand-dot { width: 84px; height: 84px; border-radius: 50%; background: var(--brand-blue); }
  .brand-name {
    font-family: "Roboto", sans-serif; font-weight: 400;
    font-size: 30px; color: var(--brand-blue); letter-spacing: 1px;
  }
  .website {
    position: absolute; right: 50px; top: 322px;
    font-family: "Roboto", sans-serif; font-size: 15px; letter-spacing: 2px;
    color: var(--brand-blue);
  }
</style>
</head>
<body>
  <div class="card">
    <svg class="card-shapes" width="1080" height="606" viewBox="0 0 1080 606">
      <defs>
        <linearGradient id="photoTone" x1="0" y1="0" x2="0" y2="1">
          <stop offset="0" stop-color="#8fb6dc"/>
          <stop offset="0.55" stop-color="#4d7fb3"/>
          <stop offset="1" stop-color="#9aa3ad"/>
        </linearGradient>
      </defs>
      <polygon role="img" aria-label="Photo of the bodyshop building" points="420,0 720,0 770,380 690,606 520,606 560,230" fill="url(#photoTone)"/>
      <polygon class="logo-panel" points="700,0 1080,0 1080,380 770,380" fill="var(--card-white)"/>
      <polygon class="accent-stripe" points="640,0 700,0 775,375 715,375" fill="var(--brand-deep)"/>
      <polygon class="corner-block" points="690,606 820,380 1080,380 1080,606" fill="var(--brand-blue)"/>
      <polygon class="corner-shade" points="820,380 1080,380 1080,470" fill="var(--brand-mid)"/>
      <polygon class="contact-panel" points="0,233 490,233 660,500 0,500" fill="var(--card-white)"/>
      <polygon class="name-band" points="0,108 520,108 560,233 0,233" fill="var(--brand-blue)"/>
      <rect class="badge-strip" x="0" y="492" width="690" height="70" fill="var(--card-white)"/>
      <line x1="0" y1="496" x2="690" y2="496" stroke="var(--rule-grey)" stroke-width="2"/>
      <line x1="0" y1="556" x2="690" y2="556" stroke="var(--rule-grey)" stroke-width="2"/>
      <g class="partner-badges" fill="var(--badge-grey)">
        <rect x="66" y="518" width="44" height="10" rx="5"/>
        <ellipse cx="160" cy="523" rx="22" ry="10" fill="#2f6b3a"/>
        <rect x="208" y="518" width="52" height="10" rx="2" fill="#c63a3a"/>
        <circle cx="300" cy="523" r="13" fill="#3b5fa0"/>
        <rect x="330" y="516" width="44" height="14" rx="7"/>
        <rect x="396" y="513" width="24" height="22" rx="3" fill="#b4343a"/>
        <rect x="440" y="515" width="30" height="16" rx="3" fill="#a83b3b"/>
        <ellipse cx="508" cy="523" rx="24" ry="12" fill="#d13a3a"/>
        <circle cx="563" cy="523" r="13"/>
      </g>
      <rect class="base-bar" x="0" y="578" width="700" height="28" fill="var(--brand-blue)"/>
    </svg>

    <div class="staff-name">MALCOLM ASHFORD</div>
    <div class="staff-role">EXECUTIVE</div>

    <div class="contact">
      <div class="company">Halden Rowe - Car Body Accident Repair</div>
      <div>Kestrel Way, Elmfield Park, Redbrook,</div>
      <div>Avonford AF12 7QT, United Kingdom</div>
      <div><span class="label">Tel:</span>0140 555 0182</div>
      <div><span class="label">Email:</span>info@haldenrowe.co.uk</div>
      <div><span class="label">Fax:</span>0140 555 0197</div>
    </div>

    <div class="brand">
      <div class="brand-dot"></div>
      <div class="brand-name">HALDEN ROWE</div>
    </div>

    <div class="website">www.haldenrowe.co.uk</div>
  </div>
</body>
</html>
```